Updated flyer

we are a defence industry trainer and we are updating a course that has been running for a few years, so want a new look flyer. Please note that the flyer is A4 and we would like people to fill in the document online. Please add a tickbox for SME's free and add a call out box saying the course is NEW & UPDATED.

Industry/Entity Type

Defence

Font styles to use
Sans Serif
Other font styles liked:
• AVENIR

Colors
3176b5
01a88e
9bcb3b
fbed22
f37022

```html
<!DOCTYPE html>
<html lang="en">
<head>
<meta charset="utf-8">
<title>Defence, ITAR &amp; EAR Training Controls – Course Flyer</title>
<link rel="stylesheet" href="https://fonts.googleapis.com/css2?family=Arimo:wght@400;700&family=Roboto+Condensed:wght@400;500;700&family=Roboto+Slab:wght@400;700&family=Crimson+Text:ital@1&display=swap">
<style>
:root{
  --blue:#1c8bb5;
  --blue-dark:#1f6f9a;
  --teal:#01a88e;
  --green:#3f8a2c;
  --lime:#9bcb3b;
  --red:#e3261c;
  --ink:#1d1d1b;
  --grey:#555;
  --field:#e4e4e4;
  --frame:#3a8fc0;
  --paper:#ffffff;
  --bg:#ffffff;
}
*{box-sizing:border-box;margin:0;padding:0}
html,body{width:1200px;height:834px;overflow:hidden;background:var(--bg)}
body{position:relative;font-family:"Arimo",Arial,sans-serif;color:var(--ink)}
.page{position:absolute;top:6px;width:590px;height:822px;background:var(--paper);border:1.5px solid var(--frame);overflow:hidden}
.page--intro{left:6px}
.page--register{left:604px}

/* masthead */
.brand{position:absolute;left:150px;top:30px;display:flex;align-items:center;gap:12px}
.brand__dot{width:72px;height:72px;border-radius:50%;background:var(--lime);flex:none}
.brand__name{font-family:"Roboto Condensed",sans-serif;font-weight:500;color:var(--teal);font-size:19px;line-height:1.08;width:190px}
.callout{position:absolute;right:8px;top:2px;width:150px;height:120px}
.callout text{font-family:"Arimo",sans-serif;font-weight:700;font-size:21px;fill:var(--ink)}
.title{position:absolute;left:0;right:0;top:134px;text-align:center;font-family:"Roboto Condensed",sans-serif;font-weight:700;font-size:26px;color:var(--blue);letter-spacing:.2px}
.subtitle{position:absolute;left:0;right:0;top:166px;text-align:center;font-family:"Roboto Condensed",sans-serif;font-size:20px;color:var(--ink);letter-spacing:.4px}

/* intro page */
.intro{position:absolute;left:20px;right:20px;top:204px;font-size:11.3px;line-height:1.45;text-align:justify}
.intro p+p{margin-top:6px}
.intro .lead{font-family:"Roboto Slab",serif;font-weight:700;color:var(--blue);font-size:13.5px}
.photo{position:absolute;left:16px;top:314px;width:556px;height:226px;background:linear-gradient(120deg,#dfe6ea 0%,#c9b29c 35%,#5a6b7c 60%,#d8e3ea 100%)}
.quotes{position:absolute;left:16px;top:550px;width:350px;text-align:right;font-family:"Crimson Text",serif;font-style:italic;font-size:14.6px;line-height:20.4px}
.dates{position:absolute;left:374px;top:552px;width:198px;height:106px;border:1.5px solid var(--frame);padding:4px 8px;font-family:"Roboto Slab",serif;font-size:13px;line-height:20px}
.dates__row{display:flex;justify-content:space-between;border-bottom:1px solid #9cc3da}
.dates__row:last-child{border-bottom:0}
.price{position:absolute;left:0;right:0;top:666px;text-align:center;font-family:"Roboto Slab",serif;font-weight:700;font-size:25px;color:var(--green)}
.price small{font-weight:400;font-size:13px}
.sme-band{position:absolute;left:0;right:0;top:706px;height:32px;background:var(--blue);color:#fff;text-align:center;font-family:"Roboto Slab",serif;font-size:17px;line-height:32px}
.sme-band b{font-weight:700}
.subsidy{position:absolute;left:0;right:0;top:750px;text-align:center;font-family:"Roboto Slab",serif;font-size:13px}
.contact-line{position:absolute;left:0;right:0;top:772px;text-align:center;font-family:"Roboto Slab",serif;font-size:13px}
.footer{position:absolute;left:0;right:0;top:792px;text-align:center;font-family:"Roboto Slab",serif;font-weight:700;font-size:15.5px}
.footer small{font-weight:400;font-size:13px}

/* register page */
.panel{position:absolute;top:200px;border:1.5px solid var(--frame);border-top:0}
.panel--content{left:12px;width:244px;height:508px}
.panel--form{left:264px;width:314px;height:508px}
.panel__head{height:30px;background:var(--blue);color:#fff;font-family:"Roboto Condensed",sans-serif;font-size:17px;line-height:30px;text-align:center;letter-spacing:.3px;margin:0 -1.5px}
.panel--form .panel__head{font-size:20px}
.topics{list-style:none;padding:10px 8px 0 10px;font-size:9.3px;line-height:11.5px}
.topics li{position:relative;padding-left:7px}
.topics li::before{content:"";position:absolute;left:0;top:4px;width:3px;height:3px;background:var(--ink)}
.form{padding:12px 8px 0 10px;font-size:11px}
.field{display:flex;align-items:center;height:19.4px}
.field__label{width:58px}
.field__box{flex:1;height:15px;background:var(--field)}
.field--wide .field__label{width:72px}
.field--card{padding-left:34px}
.field--card .field__label{width:72px}
.opts{display:flex;gap:18px;height:19.4px;align-items:center}
.tick{display:inline-block;width:7px;height:7px;border:1px solid var(--ink);margin-right:5px;vertical-align:0}
.note{font-size:8.5px;font-style:italic;color:var(--grey);margin:4px 0 6px}
.note-h{font-size:11px;margin-top:2px}
.note-h i{font-size:8.5px;color:var(--grey)}
.locations{padding-left:34px;font-size:9.6px;line-height:12.5px;margin-bottom:6px}
.howto{font-size:10.5px;line-height:13px}
.office{margin-top:5px;font-size:8.5px}
.office__grid{display:grid;grid-template-columns:1fr 1fr;font-size:7px;color:var(--grey);margin-top:4px;row-gap:2px}
.policy{position:absolute;left:14px;right:14px;top:716px}
.policy h3{font-size:12px;font-weight:700}
.policy p{font-size:8.6px;line-height:12px;color:var(--grey);margin-top:4px}
.policy .web{text-align:center;font-size:9.5px;color:var(--ink);margin-top:6px}
.policy .web b{font-weight:700}
</style>
</head>
<body>

<!-- Side one: course overview -->
<section class="page page--intro">
  <div class="brand">
    <span class="brand__dot"></span>
    <span class="brand__name">Institute for Trade Compliance Training</span>
  </div>
  <svg class="callout" viewBox="0 0 150 120" aria-label="New and updated">
    <path d="M75 8 C115 8 142 28 142 54 C142 80 115 98 75 98 C66 98 58 97 51 95 L34 116 L38 90 C18 82 8 68 8 54 C8 28 35 8 75 8 Z" fill="#fff" stroke="#e3261c" stroke-width="6"/>
    <text x="78" y="50" text-anchor="middle" transform="rotate(10 78 50)">New &amp;</text>
    <text x="76" y="74" text-anchor="middle" transform="rotate(10 76 74)">Updated</text>
  </svg>
  <h1 class="title">DEFENCE, ITAR &amp; EAR TRAINING CONTROLS</h1>
  <h2 class="subtitle">FROM A NON-U.S. PERSPECTIVE TRAINING</h2>

  <div class="intro">
    <p><span class="lead">U.S. Export Controls</span> are some of the most complex and stringent in the world. The U.S. Government regulates the transfer of U.S. origin goods and technical data throughout the world, with the intent of preventing unauthorised transfer of technology and know-how. These controls extend world-wide and can impact anyone dealing in U.S. controlled goods or technology.</p>
    <p><span class="lead">This two-day comprehensive course</span> will give applicants a greater understanding of U.S. Export Controls from a non-U.S. perspective in practical and relevant terms.</p>
  </div>

  <div class="photo" role="img" aria-label="Photograph of smiling course participants seated in a training room"></div>

  <div class="quotes">
    <p>“Excellent structure and style of presentation.”</p>
    <p>“Excellent...best U.S export controls training I have attended.”</p>
    <p>“Practical workshops were fantastic.”</p>
    <p>“Excellent presenter and coordination.”</p>
    <p>“Very informative, well presented course.”</p>
  </div>
  <div class="dates">
    <div class="dates__row"><span>Brisbane</span><span>16 &amp; 17 March</span></div>
    <div class="dates__row"><span>Sydney</span><span>18 &amp; 19 March</span></div>
    <div class="dates__row"><span>Canberra</span><span>20 &amp; 23 March</span></div>
    <div class="dates__row"><span>Melbourne</span><span>24 &amp; 25 March</span></div>
    <div class="dates__row"><span>Adelaide</span><span>26 &amp; 27 March</span></div>
  </div>

  <p class="price">$1295.00 AUD per person <small>(inc GST)</small></p>
  <div class="sme-band">Small to Medium Enterprises <b>FREE OF CHARGE</b></div>
  <p class="subsidy">Subsidised by the Regional Defence Industry Fund (RDIF)</p>
  <p class="contact-line">For more information, please contact</p>
  <p class="footer">ITCT <small>on</small> +61 (0)7 5550 1234 | hello@itct-training.com | www.itct-training.com</p>
</section>

<!-- Side two: content and registration -->
<section class="page page--register">
  <div class="brand">
    <span class="brand__dot"></span>
    <span class="brand__name">Institute for Trade Compliance Training</span>
  </div>
  <svg class="callout" viewBox="0 0 150 120" aria-label="New and updated">
    <path d="M75 8 C115 8 142 28 142 54 C142 80 115 98 75 98 C66 98 58 97 51 95 L34 116 L38 90 C18 82 8 68 8 54 C8 28 35 8 75 8 Z" fill="#fff" stroke="#e3261c" stroke-width="6"/>
    <text x="78" y="50" text-anchor="middle" transform="rotate(10 78 50)">New &amp;</text>
    <text x="76" y="74" text-anchor="middle" transform="rotate(10 76 74)">Updated</text>
  </svg>
  <h1 class="title">DEFENCE, ITAR &amp; EAR TRAINING CONTROLS</h1>
  <h2 class="subtitle">FROM A NON-U.S. PERSPECTIVE TRAINING</h2>

  <div class="panel panel--content">
    <div class="panel__head">2 DAY COURSE CONTENT</div>
    <ul class="topics">
      <li>Export Control terms and conditions</li>
      <li>Export Control Reform and the impact to Australian industry</li>
      <li>Managing reclassifications</li>
      <li>Applying deminimis</li>
      <li>Understanding 600 Series &amp; limitations</li>
      <li>Understanding the Commerce Country List, Country Chart &amp; Country Groups</li>
      <li>Understanding deemed exports</li>
      <li>EAR General Prohibitions</li>
      <li>U.S. export controls jurisdictions</li>
      <li>Relevant legislation</li>
      <li>Understand U.S. authorisations</li>
      <li>Sub-licensing options &amp; requirements</li>
      <li>Applying U.S. exemptions</li>
      <li>Understanding re-exports &amp; how to obtain authorisation</li>
      <li>Australian export controls</li>
      <li>Australian / U.S. Trade Co-operation Treaty</li>
      <li>Dual &amp; third country national issues &amp; exemptions</li>
      <li>Developing a compliance framework</li>
      <li>Clound Computing &amp; other technical issues</li>
      <li>Managing multi-jurisdictions</li>
      <li>Identifying the best authorisations to use</li>
      <li>Recordk-keeping &amp; administrative requirements</li>
      <li>Understanding FMS</li>
      <li>Creating a monitoring &amp; self-assessment process</li>
      <li>Managing violations</li>
      <li>Non-compliance &amp; fines</li>
      <li>Case Studies</li>
      <li>Best practice principles</li>
      <li>Strategic planning</li>
    </ul>
  </div>

  <div class="panel panel--form">
    <div class="panel__head">REGISTER ONLINE OR BELOW</div>
    <div class="form">
      <div class="field"><span class="field__label">Name:</span><span class="field__box"></span></div>
      <div class="field"><span class="field__label">Company:</span><span class="field__box"></span></div>
      <div class="field"><span class="field__label">Address:</span><span class="field__box"></span></div>
      <div class="field"><span class="field__label">Mobile no:</span><span class="field__box"></span></div>
      <div class="field"><span class="field__label">Email:</span><span class="field__box"></span></div>
      <div class="field field--wide"><span class="field__label">Dietary needs:</span><span class="field__box"></span></div>
      <p class="note-h">Payment method: <i>(please check one)</i></p>
      <div class="opts"><span><span class="tick"></span>Invoice</span><span><span class="tick"></span>Free of Charge (SME)</span></div>
      <div class="opts"><span><span class="tick"></span>Credit card*</span></div>
      <div class="opts" style="padding-left:34px;gap:8px"><span>Card type:</span><span><span class="tick"></span>Credit</span><span><span class="tick"></span>Debit</span><span><span class="tick"></span>Charge card</span></div>
      <div class="field field--card"><span class="field__label">Card name:</span><span class="field__box"></span></div>
      <div class="field field--card"><span class="field__label">Card number:</span><span class="field__box"></span></div>
      <div class="field field--card"><span class="field__label">Expiry date:</span><span class="field__box"></span></div>
      <div class="field field--card"><span class="field__label" style="width:88px">Cardholder email:</span><span class="field__box"></span></div>
      <p class="note">Credit card payments incur a 2.5% surcharge. Charge cards incur 3%.</p>
      <p class="note-h">Course location: <i>(please check)</i></p>
      <div class="locations">
        <p><span class="tick"></span>Brisbane 16 &amp; 17 March</p>
        <p><span class="tick"></span>Sydney 18 &amp; 19 March</p>
        <p><span class="tick"></span>Canberra 20 &amp; 23 March</p>
        <p><span class="tick"></span>Melbourne 24 &amp; 25 March</p>
        <p><span class="tick"></span>Adelaide 26 &amp; 27 March</p>
      </div>
      <div class="howto">
        <p>Register online @ tradecourses.example/events</p>
        <p>or/.. email registrations to hello@itct-training.com</p>
        <p>or/.. fax to +61 (0)7 5550 5678</p>
      </div>
      <div class="office">
        <p>OFFICE USE ONLY:</p>
        <div class="office__grid">
          <span>Confirmation sent: ..............................</span><span>Invoice no: ..............................</span>
          <span>Contact person: ..............................</span><span>Paid: ......................................</span>
        </div>
      </div>
    </div>
  </div>

  <div class="policy">
    <h3>Cancellation Policy:</h3>
    <p>Cancellations incur a 20% administration fee. No cancellations permitted within 30 days of training commencing. If a registered attendee is unable to attend, a replacement attendee is allowed.</p>
    <p class="web">REGISTER ONLINE @ <b>tradecourses.example/events</b></p>
  </div>
  <p class="footer">+61 (0)7 5550 1234 | hello@itct-training.com | www.itct-training.com</p>
</section>

</body>
</html>
```